Harbor Rest Company Needs Business Card

Looking for a very nice looking business card. Creative but not extravagant. We sell beds and pillows across the U.S. and need something professional but catchy. I have attached the logo.

Name : Dale Morton
Title : President
Phone : (800) 417-2960
Email: rest@quiltano.com
Website: www.quiltano.com

Can be single-sided or double-sided
horizontal or vertical

Can use Blues/Greys

Target Market(s)

Mass Market

Industry/Entity Type

Retail

Contact Information for Business Card

Name : Dale Morton
Title : President
Phone : (800) 417-2960
Email: rest@quiltano.com
Website: www.quiltano.com

Requirements
Must have
• Clean, Modern, Smooth
• Can use Blues/Greys
• On the other side without the information - have something simple like www.quiltano.com or our logo
Nice to have
• Surprise me
Should not have
• Nothing crazy, nothing cluttered

```html
<!DOCTYPE html>
<html lang="en">
<head>
<meta charset="utf-8">
<title>Quiltano Business Card</title>
<link rel="stylesheet" href="https://fonts.googleapis.com/css2?family=Lato:ital,wght@0,400;0,700;1,400&display=swap">
<style>
  :root {
    --page-bg: #e4e7ea;
    --card-bg: #f4f6f7;
    --card-edge: #c8d0d7;
    --brand-blue: #2b7fc1;
    --name-blue: #1d4f7c;
    --text-grey: #4a5560;
    --title-dark: #2a2f35;
    --icon-blue: #2f6f9e;
    --band-start: #2a6da3;
    --band-end: #1c4f7d;
    --band-text: #b7c6d4;
  }
  html, body {
    margin: 0;
    width: 1200px;
    height: 970px;
    overflow: hidden;
    background: var(--page-bg);
  }
  .card {
    position: absolute;
    left: 100px;
    top: 186px;
    width: 1000px;
    height: 597px;
    background: var(--card-bg);
    border: 1px solid var(--card-edge);
    box-sizing: border-box;
    overflow: hidden;
  }
  .brand-name {
    position: absolute;
    left: 0;
    right: 0;
    top: 78px;
    margin: 0;
    text-align: center;
    font-family: "Lato", sans-serif;
    font-weight: 400;
    font-size: 140px;
    line-height: 1;
    letter-spacing: 2px;
    color: var(--brand-blue);
  }
  .contact {
    position: absolute;
    left: 64px;
    top: 384px;
    margin: 0;
    padding: 0;
    list-style: none;
    font-family: "Lato", sans-serif;
    font-size: 23px;
    color: var(--text-grey);
  }
  .contact li {
    display: flex;
    align-items: center;
    height: 44px;
  }
  .contact svg {
    width: 26px;
    height: 22px;
    margin-right: 10px;
    fill: var(--icon-blue);
  }
  .person {
    position: absolute;
    right: 86px;
    top: 388px;
    text-align: right;
    font-family: "Lato", sans-serif;
  }
  .person-name {
    margin: 0;
    font-weight: 700;
    font-size: 29px;
    line-height: 1.1;
    color: var(--name-blue);
  }
  .person-title {
    margin: 2px 0 0;
    font-style: italic;
    font-size: 21px;
    color: var(--title-dark);
  }
  .web-band {
    position: absolute;
    left: 0;
    right: 0;
    bottom: 0;
    height: 60px;
    background: linear-gradient(90deg, var(--band-start), var(--band-end));
    display: flex;
    align-items: center;
    justify-content: center;
    font-family: "Lato", sans-serif;
    font-weight: 700;
    font-size: 20px;
    letter-spacing: 5px;
    color: var(--band-text);
  }
</style>
</head>
<body>
  <div class="card">
    <h1 class="brand-name">quiltano</h1>

    <ul class="contact">
      <li>
        <svg viewBox="0 0 26 22" aria-hidden="true">
          <path d="M3 7c0-3 4-5 10-5s10 2 10 5v2h-5V7c-1-1-3-1.5-5-1.5S9 6 8 7v2H3z"/>
          <path d="M7 10h12l3 9H4z M11 13a2 2 0 1 0 4 0a2 2 0 1 0-4 0z"/>
        </svg>
        (800) 417-2960
      </li>
      <li>
        <svg viewBox="0 0 26 22" aria-hidden="true">
          <path d="M2 3h22v16H2z M4 5v1l9 6 9-6V5z" fill-rule="evenodd"/>
        </svg>
        rest@quiltano.com
      </li>
    </ul>

    <div class="person">
      <p class="person-name">Dale Morton</p>
      <p class="person-title">President</p>
    </div>

    <div class="web-band">www.quiltano.com</div>
  </div>
</body>
</html>
```